Vegan bakery needs business card

We need a business card design for my vegan bakery in Philadelphia Pa. We create amazing whole food plant based cuisine that is egg and dairy free. We use fruits, vegetables, healing herbs, nuts, natural sugars (date, turbinado, agave) and non bleached flours in our creations. Due to demand and interest in the Philadelphia area we created a late night vegan dessert delivery service named Moonlark Greens. We are the only business providing delicious vegan desserts delivered to your door at 1am!! We would like to see designs that use the color scheme in the logo. The final design should communicate the benefits of our products: dairy/egg free, plant based, healing herbs, amazing food.

Industry/Entity Type

Business

```html
<!DOCTYPE html>
<html lang="en">
<head>
<meta charset="utf-8">
<title>Moonlark Greens – Business Card</title>
<link rel="stylesheet" href="https://fonts.googleapis.com/css2?family=Questrial&display=swap">
<style>
  :root {
    --backdrop: #dcdbdc;
    --paper: #ffffff;
    --coral: #f26b4f;
    --leaf: #6cc04a;
    --ink: #6d6d6d;
    --shadow: rgba(0,0,0,0.18);
  }
  * { box-sizing: border-box; margin: 0; padding: 0; }
  html, body { width: 1200px; height: 837px; overflow: hidden; }
  body {
    background: var(--backdrop);
    font-family: "Questrial", "Century Gothic", sans-serif;
    display: flex;
    align-items: center;
    justify-content: center;
    gap: 48px;
  }
  .card {
    position: relative;
    width: 532px;
    height: 304px;
    background: var(--paper);
    box-shadow: 0 8px 24px var(--shadow);
    overflow: hidden;
  }
  .brand {
    position: absolute;
    display: flex;
    flex-direction: column;
    align-items: center;
  }
  .brand-mark {
    display: flex;
    align-items: center;
    gap: 8px;
  }
  .brand-dot {
    width: 22px; height: 22px;
    border-radius: 50%;
    background: var(--coral);
  }
  .brand-name {
    color: var(--coral);
    font-size: 27px;
    letter-spacing: 0.5px;
  }
  .tagline {
    margin-top: 8px;
    color: var(--leaf);
    font-size: 16px;
    line-height: 1.1;
    text-align: center;
  }
  .rule {
    position: absolute;
    height: 1.5px;
    background: var(--leaf);
  }

  /* front face */
  .card-front .brand { left: 0; right: 0; top: 78px; }
  .card-front .rule-left { left: 0; width: 190px; top: 212px; }
  .card-front .rule-right { left: 342px; right: 0; top: 212px; }
  .products-label {
    position: absolute;
    left: 190px; width: 152px;
    top: 204px;
    text-align: center;
    color: var(--leaf);
    font-size: 13px;
    letter-spacing: 0.5px;
  }
  .products-list {
    position: absolute;
    left: 0; right: 0;
    top: 232px;
    text-align: center;
    color: var(--coral);
    font-size: 15px;
  }

  /* back face */
  .card-back .brand { left: 34px; width: 230px; top: 70px; }
  .card-back .brand-name { font-size: 24px; }
  .card-back .rule-left { left: 0; width: 292px; top: 186px; }
  .card-back .rule-bottom { left: 446px; right: 0; top: 274px; }
  .contact {
    position: absolute;
    left: 300px;
    top: 92px;
    color: var(--ink);
    font-size: 13px;
    line-height: 1.35;
  }
  .person-name { color: var(--coral); font-size: 19px; line-height: 1.1; }
  .person-title { font-size: 12.5px; margin-bottom: 10px; }
  .contact-line { display: flex; align-items: center; gap: 6px; }
  .contact-icon {
    width: 13px; height: 13px;
    border-radius: 50%;
    background: var(--coral);
    display: flex; align-items: center; justify-content: center;
  }
  .address { margin-top: 8px; }
  .address-name { color: var(--coral); }
  .website {
    position: absolute;
    left: 268px;
    top: 265px;
    color: var(--leaf);
    font-size: 14px;
  }
</style>
</head>
<body>

  <section class="card card-front" aria-label="Card front">
    <div class="brand">
      <div class="brand-mark">
        <span class="brand-dot"></span>
        <span class="brand-name">Moonlark Greens</span>
      </div>
      <p class="tagline">100% vegan<br>100% delicious</p>
    </div>
    <div class="rule rule-left"></div>
    <p class="products-label">OUR PRODUCTS</p>
    <div class="rule rule-right"></div>
    <p class="products-list">dairy/egg free, plant based, healing herbs, amazing food.</p>
  </section>

  <section class="card card-back" aria-label="Card back">
    <div class="brand">
      <div class="brand-mark">
        <span class="brand-dot"></span>
        <span class="brand-name">Moonlark Greens</span>
      </div>
      <p class="tagline">100% vegan<br>100% delicious</p>
    </div>
    <div class="rule rule-left"></div>

    <div class="contact">
      <p class="person-name">Tobias Wren</p>
      <p class="person-title">Director of Marketing</p>
      <p class="contact-line">
        <span class="contact-icon">
          <svg width="8" height="8" viewBox="0 0 24 24" aria-hidden="true"><path fill="#fff" d="M6.6 10.8a15.1 15.1 0 0 0 6.6 6.6l2.2-2.2c.3-.3.7-.4 1-.2 1.1.4 2.3.6 3.6.6.6 0 1 .4 1 1V20c0 .6-.4 1-1 1C10.6 21 3 13.4 3 4c0-.6.4-1 1-1h3.5c.6 0 1 .4 1 1 0 1.3.2 2.5.6 3.6.1.3 0 .7-.2 1z"/></svg>
        </span>215-555-0147
      </p>
      <p class="contact-line">
        <span class="contact-icon">
          <svg width="8" height="8" viewBox="0 0 24 24" aria-hidden="true"><rect x="7" y="2" width="10" height="20" rx="2" fill="#fff"/></svg>
        </span>215-555-0148
      </p>
      <p class="contact-line">
        <span class="contact-icon">
          <svg width="8" height="8" viewBox="0 0 24 24" aria-hidden="true"><rect x="2" y="5" width="20" height="14" rx="1" fill="#fff"/><path d="M2 6l10 7 10-7" stroke="#f26b4f" stroke-width="2" fill="none"/></svg>
        </span>hello@moonlarkgreens.com
      </p>
      <p class="address">
        <span class="address-name">Moonlark Greens</span><br>
        PO Box 418, Larkspur Street<br>
        Philadelphia, PA 19107
      </p>
    </div>

    <p class="website">www.moonlarkgreens.com</p>
    <div class="rule rule-bottom"></div>
  </section>

</body>
</html>
```